Warm Hands Close Deals.

Sub: how friendliness wins every bargain.

The book talks about what you need to do to achieves a better atmosphere and what you need to do warm your customer. It provides techniques on how to talk, move and about how to create rapport using content, hobbies, common interests and so on. All to increase success in selling something, convincing somebody and being liked much more. It extends to the claim that convincing your spouse to chose your favorite movie rather than hers or to pick that vacation sport over the other one would also a sale, not a commercial sale but an important one too. And that you can achieve these kind of success too using the information from the book. However this is NOT a self help book but a business book!

Business

```html
<!DOCTYPE html>
<html lang="en">
<head>
<meta charset="UTF-8">
<title>Warm Hands Close Deals. — Book Cover</title>
<link rel="stylesheet" href="https://fonts.googleapis.com/css2?family=Bebas+Neue&display=swap">
<style>
  :root {
    --page-bg: #eeeeef;
    --cover-white: #ffffff;
    --band-purple: #6e2fa0;
    --author-purple: #5b2588;
    --subtitle-grey: #6f6f6f;
    --band-text: #ffffff;
    --photo-dark: #2b3344;
    --photo-mid: #7f8a99;
    --photo-light: #d9dde2;
  }
  * { box-sizing: border-box; margin: 0; padding: 0; }
  html, body {
    width: 1112px;
    height: 1200px;
    overflow: hidden;
    background: var(--page-bg);
  }
  .canvas {
    position: relative;
    width: 1112px;
    height: 1200px;
  }
  .book-cover {
    position: absolute;
    left: 216px;
    top: 50px;
    width: 680px;
    height: 1100px;
    background: var(--cover-white);
    box-shadow: 0 18px 40px rgba(0,0,0,0.18);
    overflow: hidden;
  }
  .cover-photo {
    position: absolute;
    left: 0;
    top: 0;
    width: 680px;
    height: 544px;
    background:
      radial-gradient(ellipse at 60% 40%, rgba(255,255,255,0.35), transparent 60%),
      linear-gradient(100deg, var(--photo-dark) 0%, var(--photo-mid) 35%, var(--photo-light) 55%, var(--photo-mid) 75%, var(--photo-dark) 100%);
  }
  .title-band {
    position: absolute;
    left: 0;
    top: 540px;
    width: 680px;
    height: 80px;
    background: var(--band-purple);
    box-shadow: 0 8px 14px rgba(0,0,0,0.22);
    display: flex;
    align-items: center;
    justify-content: center;
  }
  .book-title {
    font-family: "Bebas Neue", "Arial Narrow", sans-serif;
    font-weight: 400;
    font-size: 66px;
    line-height: 1;
    letter-spacing: 0.5px;
    color: var(--band-text);
    padding-top: 6px;
  }
  .book-subtitle {
    position: absolute;
    left: 0;
    top: 672px;
    width: 680px;
    text-align: center;
    font-family: "Bebas Neue", "Arial Narrow", sans-serif;
    font-weight: 400;
    font-size: 78px;
    line-height: 74px;
    color: var(--subtitle-grey);
  }
  .book-subtitle span { display: block; }
  .author-name {
    position: absolute;
    left: 0;
    top: 988px;
    width: 680px;
    text-align: center;
    font-family: "Bebas Neue", "Arial Narrow", sans-serif;
    font-weight: 400;
    font-size: 56px;
    line-height: 1;
    color: var(--author-purple);
  }
</style>
</head>
<body>
  <main class="canvas">
    <section class="book-cover">
      <div class="cover-photo" role="img" aria-label="Photo of two business people in suits shaking hands across an office desk, one holding a grey folder with a winking cartoon face, shelves of binders behind"></div>
      <div class="title-band">
        <h1 class="book-title">WARM HANDS CLOSE DEALS.</h1>
      </div>
      <h2 class="book-subtitle">
        <span>HOW FRIENDLINESS</span>
        <span>WINS EVERY</span>
        <span>BARGAIN.</span>
      </h2>
      <p class="author-name">AUTHOR NAME</p>
    </section>
  </main>
</body>
</html>
```